PSD website for property company

Please read the brief thoroughly.

We are looking for a new website for a property group that does property acquisitions, property development and property management.
They buy, build and lease core inner city industrial assets in Sydney, Australia.
They also invest in residential developments.

Site menu
- Home page
- Property – sub menus include – Leasing ; Projects ; Investments ; Property Management
- Capital and finance
- About
- Contact

They like this website
https://www.verlo.com.au/

They want the site to be clean, modern and bold.
They like few colors, even black and white is OK to submit

They have a logo and style guide and useable images here:
http://www.kumet.net/temp/PelorisWeb2019.zip
The zip file is also attached to this project.
We have supplied some images to give you an idea, but we will also require you to provide at least 3 extra images from stock photos.
Use your imagination.

I am expecting a lot of similar designs, so be aware the photos you choose will be really important.
They want really 3 good stock photos used and supplied without charge.
Please not too generic, I repeat the quality of the photos is important.
You may provide several photos (but not in multiple submissions please) and we will choose the best three to be provided.

The winner will be selected on a single home page design and required to provide;
All photos use in original format without charge
A second ‘standard page’ template design based on the winning home page design

```html
<!DOCTYPE html>
<html lang="en">
<head>
<meta charset="utf-8">
<title>Peloris – Property Group</title>
<link href="https://fonts.googleapis.com/css2?family=Josefin+Sans:wght@300;400;600;700&display=swap" rel="stylesheet">
<style>
:root{
  --green:#8fa98a;
  --green-dark:#7f9a7a;
  --ink:#2b2b2b;
  --text:#555;
  --grey-band:#808080;
  --light:#e9e9e9;
  --white:#fff;
  --navy:#2e3747;
}
*{box-sizing:border-box;margin:0;padding:0}
html,body{width:1200px;height:3628px;overflow:hidden}
body{position:relative;background:var(--white);font-family:"Josefin Sans",sans-serif;color:var(--ink)}
.abs{position:absolute}
.photo{position:absolute}

/* header */
.header-band{left:0;top:0;width:1200px;height:563px;background:var(--grey-band)}
.logo{left:111px;top:33px;font-size:44px;font-weight:700;letter-spacing:6px;color:var(--white)}
.nav{top:48px;right:111px;display:flex;gap:26px;font-size:15px;font-weight:300;color:var(--white)}
.nav .active{font-weight:600;position:relative}
.nav .active::after{content:"";position:absolute;left:50%;top:22px;width:1px;height:32px;background:var(--white)}
.hero{left:66px;top:104px;width:1069px;height:521px;background:linear-gradient(160deg,#9fb3c4 0%,#c9d2d6 30%,#6b5141 55%,#4a3a30 80%,#3f4a3a 100%)}
.hero-title{left:111px;top:206px;font-size:62px;line-height:64px;color:var(--white);font-weight:400}
.hero-sub{left:111px;top:340px;font-size:20px;font-weight:300;color:var(--white)}
.btn-dark{left:111px;top:400px;width:149px;height:45px;background:#2a2a2a;color:var(--white);font-size:15px;display:flex;align-items:center;justify-content:center}
.dot{left:1081px;width:7px;height:7px;border:1px solid var(--white);border-radius:50%}
.dot.on{background:var(--white)}

/* about */
.h2{font-size:44px;font-weight:400;color:var(--ink)}
.h3{font-size:25px;line-height:32px;font-weight:400;color:var(--ink)}
.body{font-size:14px;line-height:17px;font-weight:300;color:var(--text)}
.btn-green{width:149px;height:45px;background:var(--green);color:var(--white);font-size:15px;display:flex;align-items:center;justify-content:center}

/* property */
.prop-band{left:0;top:1236px;width:1200px;height:648px;background:var(--light)}
.tile-label{position:absolute;left:0;right:0;bottom:0;height:39px;background:var(--green);color:var(--white);font-size:19px;padding:0 14px;display:flex;align-items:center;justify-content:space-between}
.tile-label svg{width:12px;height:18px}

/* finance */
.card{width:240px;height:221px;border:1px solid #cfcfcf;background:var(--white);text-align:center}
.card.featured{background:var(--green);border-color:var(--green)}
.card .icon{position:absolute;left:50%;top:-44px;margin-left:-44px;width:88px;height:88px;border-radius:50%;background:var(--green);display:flex;align-items:center;justify-content:center}
.card.featured .icon{background:#2a2a2a}
.card h4{margin-top:64px;font-size:22px;font-weight:400;color:var(--ink)}
.card p{margin:14px 22px 0;font-size:14px;line-height:16px;font-weight:300;color:var(--text)}
.card .more{display:block;margin-top:14px;font-size:14px;color:var(--green)}
.card.featured h4,.card.featured p,.card.featured .more{color:var(--white)}

/* testimonials */
.testi-band{left:0;top:2450px;width:1200px;height:380px;background:linear-gradient(180deg,#26303f 0%,#3a4350 60%,#2b3340 100%)}
.testi-card{width:480px;height:182px;background:var(--white)}
.avatar{left:37px;top:34px;width:77px;height:77px;border:2px solid #ddd;background:linear-gradient(180deg,#c9c2b8,#6d6a66)}
.testi-name{left:131px;top:36px;font-size:22px;color:var(--ink)}
.testi-role{left:131px;top:62px;font-size:13px;font-weight:300;color:var(--text)}
.testi-body{left:131px;top:90px;width:320px;font-size:14px;line-height:16px;font-weight:300;color:var(--text);letter-spacing:.3px}

/* contact */
.contact-bg{left:0;top:3064px;width:1200px;height:564px;background:linear-gradient(180deg,#2c3230 0%,#3d4441 60%,#262b2a 100%)}
.contact-panel{left:111px;top:2920px;width:977px;height:656px;background:var(--green)}
.check{width:24px;height:24px;border:1px solid var(--white)}
.check-label{font-size:15px;color:var(--white);letter-spacing:1px}
.field{height:35px;background:var(--white);color:#999;font-size:13px;padding:11px 12px;letter-spacing:.5px}
.submit{left:541px;top:3326px;width:117px;height:35px;background:var(--white);color:var(--ink);font-size:13px;letter-spacing:1px;display:flex;align-items:center;justify-content:center}
.foot-h{font-size:21px;color:var(--white)}
.foot-t{font-size:13px;font-weight:300;color:var(--white);letter-spacing:.8px}
.copyright{left:0;top:3596px;width:1200px;text-align:center;font-size:12px;color:var(--white);letter-spacing:.6px}
</style>
</head>
<body>

<!-- Header & hero -->
<div class="abs header-band"></div>
<div class="photo hero" role="img" aria-label="Brick apartment building with arched windows on a city street"></div>
<div class="abs logo">PELORIS</div>
<nav class="abs nav">
  <span class="active">Home</span><span>Property</span><span>Capital and Finance</span><span>About</span><span>Contact</span>
</nav>
<h1 class="abs hero-title">Lorem Ipsum Dolor<br>Sit Amet</h1>
<p class="abs hero-sub">Lorem ipsum dolor sit amet, consectetuer adipiscing elit</p>
<div class="abs btn-dark">Explore Project</div>
<span class="abs dot" style="top:293px"></span>
<span class="abs dot on" style="top:316px"></span>
<span class="abs dot" style="top:338px"></span>
<span class="abs dot" style="top:362px"></span>

<!-- About -->
<div class="photo" style="left:111px;top:715px;width:269px;height:213px;background:linear-gradient(135deg,#e8ecef,#b9bcbf)" role="img" aria-label="Model houses beside a judge's gavel"></div>
<div class="photo" style="left:387px;top:715px;width:269px;height:213px;background:linear-gradient(160deg,#7fb0d9,#e8a35a 60%,#8a6a50)" role="img" aria-label="Tower cranes over high-rise construction at sunset"></div>
<div class="photo" style="left:111px;top:935px;width:269px;height:213px;background:linear-gradient(160deg,#2f5a57,#3e6b66)" role="img" aria-label="Hand holding a piggy bank in front of a chalk house drawing"></div>
<div class="photo" style="left:387px;top:935px;width:269px;height:213px;background:linear-gradient(180deg,#a9cbe8,#eef0ee 55%,#7a8f6a)" role="img" aria-label="White modern apartment block"></div>
<h2 class="abs h2" style="left:683px;top:768px">About Us</h2>
<p class="abs h3" style="left:683px;top:835px">Lorem Ipsum Dolor Sit Amet,<br>Consectetuer Adipiscing Elit</p>
<p class="abs body" style="left:683px;top:924px;width:410px">Lorem ipsum dolor sit amet, consectetuer adipiscing elitAenean commodo ligula eget dolor. Aenean massa. Cum sociis natoque penatibus et magnis dis parturient montes, nascetur ridiculus mus. Donec quam felis, ultricies pellentesque eu, pretium quis, sem nulla consequat</p>
<div class="abs btn-green" style="left:683px;top:1045px">Read More</div>

<!-- Property -->
<div class="abs prop-band"></div>
<h2 class="abs h2" style="left:111px;top:1318px">Our Property</h2>
<p class="abs h3" style="left:111px;top:1386px;width:470px;font-size:24px;line-height:29px">Lorem Ipsum Dolor Sit Amet, Consectetuer Adipiscing Elit</p>
<p class="abs body" style="left:111px;top:1476px;width:470px">Lorem Ipsum dolor sit amet, consectetuer adipiscing elit. Aenean commodo ligula eget dolor. Aenean massa. Cum sociis natoque penatibus et magnis dis parturient montes, nascetur ridiculus mus.</p>

<div class="photo" style="left:605px;top:1326px;width:236px;height:230px;background:linear-gradient(160deg,#c79a4a,#eaeaea 55%,#8fa070)" role="img" aria-label="Modern apartment blocks with timber cladding"><div class="tile-label">Lorem Ipsum<svg viewBox="0 0 12 18"><path d="M2 1l8 8-8 8" fill="none" stroke="#fff" stroke-width="1.6"/></svg></div></div>
<div class="photo" style="left:853px;top:1326px;width:235px;height:230px;background:linear-gradient(160deg,#9bc0dc,#8a5a3a 45%,#5f7f3f)" role="img" aria-label="Apartment building with balconies among autumn trees"><div class="tile-label">Lorem Ipsum<svg viewBox="0 0 12 18"><path d="M2 1l8 8-8 8" fill="none" stroke="#fff" stroke-width="1.6"/></svg></div></div>
<div class="photo" style="left:111px;top:1567px;width:235px;height:230px;background:linear-gradient(160deg,#cfe6f2,#2f7f9a 50%,#1d4f63)" role="img" aria-label="Glass office towers seen from below"><div class="tile-label">Lorem Ipsum<svg viewBox="0 0 12 18"><path d="M2 1l8 8-8 8" fill="none" stroke="#fff" stroke-width="1.6"/></svg></div></div>
<div class="photo" style="left:359px;top:1567px;width:235px;height:230px;background:linear-gradient(160deg,#8a8f86,#e9ecec 50%,#7c9160)" role="img" aria-label="White residential buildings around a garden courtyard"><div class="tile-label">Lorem Ipsum<svg viewBox="0 0 12 18"><path d="M2 1l8 8-8 8" fill="none" stroke="#fff" stroke-width="1.6"/></svg></div></div>
<div class="photo" style="left:607px;top:1567px;width:235px;height:230px;background:linear-gradient(160deg,#e5ecef,#6f9a52 55%,#b9b3a8)" role="img" aria-label="Paved garden path between apartment buildings"><div class="tile-label">Lorem Ipsum<svg viewBox="0 0 12 18"><path d="M2 1l8 8-8 8" fill="none" stroke="#fff" stroke-width="1.6"/></svg></div></div>
<div class="photo" style="left:853px;top:1567px;width:235px;height:230px;background:linear-gradient(110deg,#b84a2a,#d98a6a 50%,#c14e2e)" role="img" aria-label="Red facade of a modern building in perspective"><div class="tile-label">Lorem Ipsum<svg viewBox="0 0 12 18"><path d="M2 1l8 8-8 8" fill="none" stroke="#fff" stroke-width="1.6"/></svg></div></div>

<!-- Capital and Finance -->
<h2 class="abs h2" style="left:0;top:1970px;width:1200px;text-align:center">Capital and Finance</h2>
<p class="abs body" style="left:0;top:2035px;width:1200px;text-align:center;font-size:14px">Lorem Ipsum dolor sit amet, consectetuer adipiscing elit.<br>Aenean commodo ligula eget dolor</p>

<div class="abs card" style="left:111px;top:2139px">
  <div class="icon"><svg width="48" height="48" viewBox="0 0 48 48" fill="none" stroke="#fff" stroke-width="1.6"><path d="M12 22l12-11 12 11M16 19v12h16V19"/><path d="M6 28c4 8 10 12 18 12s14-4 18-12"/></svg></div>
  <h4>Lorem Ipsum</h4>
  <p>Lorem Ipsumdolor sit amet, consectetuer adipiscing elit. Aenean commodo ligula eget dolor aenean massa.</p>
  <span class="more">Read More</span>
</div>
<div class="abs card featured" style="left:358px;top:2139px">
  <div class="icon"><svg width="48" height="48" viewBox="0 0 48 48" fill="none" stroke="#fff" stroke-width="1.6"><rect x="12" y="8" width="18" height="28" rx="2"/><path d="M16 16h10M16 21h10M16 26h6"/><ellipse cx="34" cy="30" rx="6" ry="2.5"/><path d="M28 30v8c0 1.4 2.7 2.5 6 2.5s6-1.1 6-2.5v-8"/></svg></div>
  <h4>Lorem Ipsum</h4>
  <p>Lorem Ipsumdolor sit amet, consectetuer adipiscing elit. Aenean commodo ligula eget dolor aenean massa.</p>
  <span class="more">Read More</span>
</div>
<div class="abs card" style="left:604px;top:2139px">
  <div class="icon"><svg width="48" height="48" viewBox="0 0 48 48" fill="none" stroke="#fff" stroke-width="1.6"><path d="M19 10h10l-3 6h-4z"/><path d="M21 16c-8 4-11 12-9 18 1 4 5 6 12 6s11-2 12-6c2-6-1-14-9-18"/><text x="24" y="34" fill="#fff" stroke="none" font-size="13" text-anchor="middle" font-family="sans-serif">$</text></svg></div>
  <h4>Lorem Ipsum</h4>
  <p>Lorem Ipsumdolor sit amet, consectetuer adipiscing elit. Aenean commodo ligula eget dolor aenean massa.</p>
  <span class="more">Read More</span>
</div>
<div class="abs card" style="left:850px;top:2139px">
  <div class="icon"><svg width="48" height="48" viewBox="0 0 48 48" fill="none" stroke="#fff" stroke-width="1.6"><rect x="10" y="9" width="28" height="30" rx="2"/><path d="M15 16h18M15 21h18M15 26h12M15 31h8"/><path d="M28 36l9-9 2 2-9 9h-2z"/></svg></div>
  <h4>Lorem Ipsum</h4>
  <p>Lorem Ipsumdolor sit amet, consectetuer adipiscing elit. Aenean commodo ligula eget dolor aenean massa.</p>
  <span class="more">Read More</span>
</div>

<!-- Testimonials -->
<div class="photo testi-band" role="img" aria-label="City skyline of high-rise towers at dusk, darkened"></div>
<h2 class="abs h2" style="left:0;top:2495px;width:1200px;text-align:center;color:var(--white)">Testimonials</h2>
<div class="abs testi-card" style="left:111px;top:2599px">
  <div class="photo avatar" role="img" aria-label="Portrait of a client in a suit"></div>
  <div class="abs testi-name">Lorem Ipsum</div>
  <div class="abs testi-role">Designation</div>
  <p class="abs testi-body">Lorem Ipsum Dolor sit amet, consectetuer adipiscing elit. Aenean commodo ligula eget dolor.Aenean massa. Cum sociis natoque penatibus et magnis dis</p>
</div>
<div class="abs testi-card" style="left:607px;top:2599px">
  <div class="photo avatar" role="img" aria-label="Portrait of a smiling client"></div>
  <div class="abs testi-name">Lorem Ipsum</div>
  <div class="abs testi-role">Designation</div>
  <p class="abs testi-body">Lorem Ipsum Dolor sit amet, consectetuer adipiscing elit. Aenean commodo ligula eget dolor.Aenean massa. Cum sociis natoque penatibus et magnis dis</p>
</div>

<!-- Contact -->
<div class="photo contact-bg" role="img" aria-label="Modern building exterior at evening, darkened"></div>
<div class="abs contact-panel"></div>
<h2 class="abs h2" style="left:0;top:2968px;width:1200px;text-align:center;color:var(--white)">Contact Us</h2>
<p class="abs" style="left:0;top:3062px;width:1200px;text-align:center;font-size:21px;color:var(--white);letter-spacing:1px">I'm inerested in</p>

<span class="abs check" style="left:231px;top:3108px"></span><span class="abs check-label" style="left:281px;top:3113px">Latest News</span>
<span class="abs check" style="left:429px;top:3108px"></span><span class="abs check-label" style="left:478px;top:3113px">Latest News</span>
<span class="abs check" style="left:628px;top:3108px"></span><span class="abs check-label" style="left:677px;top:3113px">Latest News</span>
<span class="abs check" style="left:834px;top:3108px"></span><span class="abs check-label" style="left:882px;top:3113px">Latest News</span>

<div class="abs field" style="left:231px;top:3196px;width:236px">First Name*</div>
<div class="abs field" style="left:481px;top:3196px;width:237px">First Name*</div>
<div class="abs field" style="left:732px;top:3196px;width:238px">First Name*</div>
<div class="abs field" style="left:231px;top:3243px;width:739px;height:62px">Message</div>
<div class="abs submit">SUBMIT</div>

<div class="abs" style="left:170px;top:3399px;width:870px;height:1px;background:rgba(255,255,255,.35)"></div>

<div class="abs foot-h" style="left:170px;top:3437px">Quick Links</div>
<div class="abs foot-t" style="left:170px;top:3480px;font-weight:600">Home</div>
<div class="abs foot-t" style="left:246px;top:3480px">Property</div>
<div class="abs foot-t" style="left:341px;top:3480px">Capital and Finance</div>
<div class="abs foot-t" style="left:170px;top:3505px">About</div>
<div class="abs foot-t" style="left:246px;top:3505px">Contact</div>

<div class="abs foot-h" style="left:521px;top:3437px">Address</div>
<svg class="abs" style="left:519px;top:3476px" width="12" height="17" viewBox="0 0 12 17" fill="none" stroke="#fff" stroke-width="1.4"><path d="M6 16s5-6 5-10A5 5 0 0 0 1 6c0 4 5 10 5 10z"/><circle cx="6" cy="6" r="1.8"/></svg>
<div class="abs foot-t" style="left:538px;top:3477px;width:230px;line-height:19px">123, your text will come here. Your text will come here.</div>

<svg class="abs" style="left:838px;top:3479px" width="20" height="13" viewBox="0 0 20 13" fill="none" stroke="#fff" stroke-width="1.3"><rect x="1" y="1" width="18" height="11"/><path d="M1 1l9 6 9-6"/></svg>
<div class="abs foot-t" style="left:869px;top:3478px">info.yourtext@mailbox.com</div>
<svg class="abs" style="left:842px;top:3501px" width="16" height="16" viewBox="0 0 16 16" fill="none" stroke="#fff" stroke-width="1.3"><path d="M3 1l3 3-2 2c1 2 3 4 5 5l2-2 3 3-2 3C7 14 2 9 1 3z"/></svg>
<div class="abs foot-t" style="left:869px;top:3503px">+91 000 0000 000</div>

<div class="abs copyright">Copyright © 2019 Peloris. All rights reserved.</div>

</body>
</html>
```